Family owned plumbing contractor needs eye catching business card design

Business cards that are unique, eye catching, and provide customers with general company information, such as name, address, phone number, website, employee name/title, cell phone #, & email address. We are transitioning to a new logo that utilizes a more retro feel, so we are interested in seeing some cool old school designs in the mix. We are liking the dark background on some of the samples on this website. If that is workable with our artwork, we would like to see that incorporated into the design.
Contact Information for Business Card
Copperline Pipeworks, Inc.
www.copperlinepipeworks.example
(555) 392-7068 phone
Nevada License #64205
California License #5810473
Dale Wrennick, President
(555) 618-9032 cell
dale@copperlinepipeworks.example
Residential * Commercial * Service
Requirements
Must have
- The business card details listed above & logo provided.
Nice to have
- I made some notes about color options in the description.

```html
<!DOCTYPE html>
<html lang="en">
<head>
<meta charset="utf-8">
<title>Copperline Pipeworks – Business Card</title>
<link rel="stylesheet" href="https://fonts.googleapis.com/css2?family=Lato:wght@400;700&display=swap">
<style>
  :root {
    --stage: #8a8a8a;
    --card: #1f1f1f;
    --card-back: #141414;
    --texture-light: #2a2a2a;
    --texture-dark: #0d0d0d;
    --slate: #5f7f9a;
    --teal: #5ec4ad;
    --ink: #ffffff;
    --rule: #cfcfcf;
  }
  * { box-sizing: border-box; margin: 0; padding: 0; }
  html, body { width: 1200px; height: 1200px; overflow: hidden; }
  body {
    background: var(--stage);
    font-family: "Lato", Arial, sans-serif;
    position: relative;
    color: var(--ink);
  }
  .card {
    position: absolute;
    top: 310px;
    height: 595px;
    box-shadow: 0 3px 8px rgba(0,0,0,0.35);
    overflow: hidden;
  }
  .card-front { left: 234px; width: 364px; background: var(--card); }
  .card-back  { left: 627px; width: 370px; background: var(--card-back); }

  .brand {
    position: absolute;
    left: 0; right: 0;
    display: flex;
    flex-direction: column;
    align-items: center;
    gap: 12px;
    text-align: center;
  }
  .brand-dot {
    width: 22px; height: 22px; border-radius: 50%;
    background: var(--teal);
  }
  .brand-name {
    font-weight: 700;
    font-size: 27px;
    line-height: 1.15;
    color: var(--slate);
  }
  .card-front .brand { top: 420px - 310px; top: 112px; }

  .person { position: absolute; top: 332px; left: 0; right: 0; text-align: center; }
  .person-name { font-size: 24px; color: var(--slate); letter-spacing: 0.3px; line-height: 1; }
  .person-title { font-size: 16px; margin-top: 3px; }
  .rule { width: 176px; height: 1px; background: var(--rule); margin: 10px auto 0; }

  .licenses { position: absolute; top: 392px; left: 0; right: 0; text-align: center; font-size: 16px; line-height: 21px; }

  .icon-row {
    position: absolute; top: 443px; left: 0; right: 0;
    display: flex; justify-content: center; align-items: center; gap: 3px;
  }
  .icon-row .line { width: 34px; height: 1px; background: var(--rule); margin: 0 4px; }
  .icon { width: 22px; height: 22px; }

  .contact { position: absolute; top: 473px; left: 0; right: 0; text-align: center; font-size: 16px; line-height: 21.5px; }

  .texture { position: absolute; inset: 0; }
  .card-back .brand { top: 250px; }
  .services {
    position: absolute; top: 529px; left: 0; right: 0;
    text-align: center; font-size: 16px; letter-spacing: 0.2px;
  }
  .services .sep { display: inline-block; width: 8px; height: 8px; border-radius: 50%; background: var(--ink); margin: 0 6px 2px; vertical-align: middle; }
</style>
</head>
<body>

<section class="card card-front">
  <div class="brand">
    <div class="brand-dot"></div>
    <div class="brand-name">Copperline<br>Pipeworks, Inc.</div>
  </div>

  <div class="person">
    <div class="person-name">DALE WRENNICK</div>
    <div class="person-title">President</div>
    <div class="rule"></div>
  </div>

  <div class="licenses">
    <div>Nevada License #64205</div>
    <div>California License #5810473</div>
  </div>

  <div class="icon-row">
    <span class="line"></span>
    <svg class="icon" viewBox="0 0 22 22" aria-label="phone"><circle cx="11" cy="11" r="11" fill="var(--slate)"/><path d="M6 13 Q6 9 11 9 Q16 9 16 13 L13.5 13 L13 11 L9 11 L8.5 13 Z" fill="#1f1f1f"/><rect x="7" y="13.5" width="8" height="2.5" fill="#1f1f1f"/></svg>
    <svg class="icon" viewBox="0 0 22 22" aria-label="mobile"><circle cx="11" cy="11" r="11" fill="var(--slate)"/><rect x="7.5" y="5" width="7" height="12" rx="1.2" fill="#1f1f1f"/><rect x="8.7" y="6.5" width="4.6" height="8" fill="var(--slate)"/></svg>
    <svg class="icon" viewBox="0 0 22 22" aria-label="email"><circle cx="11" cy="11" r="11" fill="var(--slate)"/><rect x="5.5" y="7" width="11" height="8" fill="#1f1f1f"/><path d="M5.5 7 L11 11.5 L16.5 7" stroke="var(--slate)" stroke-width="1" fill="none"/></svg>
    <svg class="icon" viewBox="0 0 22 22" aria-label="website"><circle cx="11" cy="11" r="11" fill="var(--slate)"/><circle cx="11" cy="11" r="5.5" fill="#1f1f1f"/><path d="M8 9 Q10 8 11 10 Q12 12 14 11" stroke="var(--slate)" stroke-width="1.3" fill="none"/></svg>
    <span class="line"></span>
  </div>

  <div class="contact">
    <div>(555) 392-7068</div>
    <div>(555) 618-9032</div>
    <div>dale@copperlinepipeworks.example</div>
    <div>www.copperlinepipeworks.example</div>
  </div>
</section>

<section class="card card-back">
  <svg class="texture" viewBox="0 0 370 595" preserveAspectRatio="none" role="img" aria-label="Distressed dark crackle texture background">
    <defs>
      <radialGradient id="backTexture" cx="45%" cy="35%" r="80%">
        <stop offset="0" stop-color="var(--texture-light)"/>
        <stop offset="1" stop-color="var(--texture-dark)"/>
      </radialGradient>
    </defs>
    <rect width="370" height="595" fill="url(#backTexture)"/>
  </svg>

  <div class="brand">
    <div class="brand-dot"></div>
    <div class="brand-name">Copperline<br>Pipeworks, Inc.</div>
  </div>

  <div class="services">RESIDENTIAL<span class="sep"></span>COMMERCIAL<span class="sep"></span> SERVICE</div>
</section>

</body>
</html>
```